Property Management company

We need a design for our company Maplecrest Elder Residences. We are complex of apartments that we manage and operate. We do like the colors green or blue

Industry/Entity Type

Property Management,

Requirements
Must have
• color
Nice to have
• maybe be able to use as a watermark

```html
<!DOCTYPE html>
<html lang="en">
<head>
<meta charset="utf-8">
<title>Maplecrest Elder Residences — Letterhead</title>
<link href="https://fonts.googleapis.com/css2?family=Poppins:wght@400;600&display=swap" rel="stylesheet">
<style>
  :root {
    --backdrop: #dcdcdc;
    --paper: #ffffff;
    --band: #1c1c1c;
    --accent: #6a9a1f;
    --text-light: #ffffff;
    --mark-grey: #a7a7a7;
    --watermark: #f4f4f4;
  }
  * { margin: 0; padding: 0; box-sizing: border-box; }
  html, body {
    width: 1200px; height: 947px; overflow: hidden;
    background: var(--backdrop);
    font-family: "Poppins", sans-serif;
  }
  .letterhead {
    position: absolute; left: 364px; top: 179px;
    width: 472px; height: 606px;
    background: var(--paper);
    overflow: hidden;
  }
  .header {
    position: absolute; left: 0; top: 0; width: 100%; height: 78px;
    background: var(--band);
    border-bottom: 3px solid var(--accent);
  }
  .brand {
    position: absolute; left: 37px; top: 16px;
    display: flex; align-items: center; gap: 14px;
  }
  .brand-dot {
    width: 44px; height: 44px; border-radius: 50%;
    background: var(--mark-grey);
  }
  .brand-name {
    color: var(--accent);
    font-weight: 600; font-size: 13px; line-height: 15px;
    letter-spacing: 0.5px; text-transform: uppercase;
  }
  .contacts {
    position: absolute; right: 27px; top: 22px;
    list-style: none;
  }
  .contacts li {
    display: flex; align-items: center; justify-content: flex-end;
    gap: 5px; height: 11.5px;
    color: var(--text-light); font-size: 8.6px;
  }
  .contacts svg { width: 9px; height: 9px; }
  .watermark {
    position: absolute; left: 100px; top: 186px;
    width: 234px; height: 234px; border-radius: 50%;
    background: var(--watermark);
  }
  .footer {
    position: absolute; left: 0; bottom: 0; width: 100%; height: 27px;
    background: var(--band);
    border-top: 3px solid var(--accent);
    display: flex; align-items: center; justify-content: center;
    color: var(--text-light); font-size: 9.4px;
  }
</style>
</head>
<body>
  <div class="letterhead">
    <header class="header">
      <div class="brand">
        <div class="brand-dot"></div>
        <div class="brand-name">Maplecrest<br>Elder Residences</div>
      </div>
      <ul class="contacts">
        <li>89897878789
          <svg viewBox="0 0 10 10" aria-hidden="true"><rect x="0.6" y="0.6" width="8.8" height="8.8" rx="1" fill="none" stroke="var(--accent)" stroke-width="1"/><path d="M3 2.5c-.6.6 0 2.3 1.6 3.9S7 8.5 7.6 7.9l.4-.6-1.3-1-.6.5C5.5 6.6 4.4 5.5 4.1 5l.5-.6-1-1.3z" fill="var(--accent)"/></svg>
        </li>
        <li>info@websitename.com
          <svg viewBox="0 0 10 10" aria-hidden="true"><rect x="0.5" y="2" width="9" height="6" fill="var(--accent)"/><path d="M0.5 2L5 5.5 9.5 2M0.5 8L4 5M9.5 8L6 5" fill="none" stroke="var(--band)" stroke-width="0.7"/></svg>
        </li>
        <li>www.website.com
          <svg viewBox="0 0 10 10" aria-hidden="true"><g fill="none" stroke="var(--accent)" stroke-width="0.8"><circle cx="5" cy="5" r="4.3"/><ellipse cx="5" cy="5" rx="1.9" ry="4.3"/><path d="M0.7 5h8.6M1.5 2.8h7M1.5 7.2h7"/></g></svg>
        </li>
      </ul>
    </header>

    <div class="watermark" aria-hidden="true"></div>

    <footer class="footer">Your Address line here, Country Code 0123456</footer>
  </div>
</body>
</html>
```